Pagebook Ads for HOA Law Firm

We need to create certain ads for a Pagebook ads campaign. We are a law firm in Florida that represents homeowners against HOAs. We need to create the following ads:

1. Image Ads Specifications:

File Type: JPG or PNG
Ratio: 1.91:1 to 4:5
Resolution:
a) 1:1 ratio: 1080 x 1080 pixels
b) 4:5 ratio: 1080 x 1350 pixels
Maximum File Size: 30MB
Minimum Width: 600 pixels
Minimum Height:
a) 1:1 ratio: 600 pixels
b) 4:5 ratio: 750 pixels
Key Elements to Include in the Ads:

1) Headline: "HOA Violating Your Rights?"
2) Main Message: "We sue HOAs for Homeowners."
3) Firm Name: Lindqvist Harrow, P.A.
4) Website: www.covenantshieldcounsel.example
5) Phone Number: 1-800-555-0148
6) Florida Bar Compliance Statement: "Serving Homeowners in Florida with our main office in Miami-Dade."
7) Call-to-Action (CTA): Include a strong CTA such as “Contact us today for a consultation!”
8) Tone and Style: Professional yet approachable. The ad should emphasize trust, expertise, and our dedication to homeowners' rights.
9) Branding: Please use our firm's brand colors and fonts. Ensure that our logo is prominently placed within the ad.
10) Image Suggestions: Consider using images of Florida homes, frustrated homeowners, or visuals that evoke trust, protection, and legal authority.

```html
<!DOCTYPE html>
<html lang="en">
<head>
<meta charset="utf-8">
<title>HOA Homeowner Ads – Lindqvist Harrow, P.A.</title>
<link href="https://fonts.googleapis.com/css2?family=Nunito+Sans:wght@400;600;700;800&display=swap" rel="stylesheet">
<style>
  :root {
    --backdrop: #f7c4a7;
    --brand-blue: #0f1689;
    --paper: #ffffff;
    --ink: #1a1a1a;
    --photo-light: #d9d9d2;
    --photo-mid: #b9bcc0;
    --photo-dark: #3f4f7e;
  }
  * { box-sizing: border-box; margin: 0; padding: 0; }
  html, body { width: 1200px; height: 800px; overflow: hidden; }
  body {
    background: var(--backdrop);
    font-family: "Nunito Sans", Arial, sans-serif;
    position: relative;
  }
  .ad {
    position: absolute;
    background: var(--paper);
    overflow: hidden;
  }
  .ad--square { left: 41px; top: 57px; width: 549px; height: 549px; }
  .ad--portrait { left: 610px; top: 57px; width: 549px; height: 686px; }

  .ad__photo {
    position: absolute; left: 0; top: 0; width: 100%;
    background:
      linear-gradient(180deg, transparent 55%, rgba(63,79,126,.55) 100%),
      linear-gradient(90deg, var(--photo-light), var(--photo-mid) 50%, var(--photo-light));
  }
  .ad--square .ad__photo { height: 246px; }
  .ad--portrait .ad__photo { height: 332px; }

  .ad__band {
    position: absolute; left: 0; width: 100%;
    background: var(--brand-blue);
    color: var(--paper);
    text-align: center;
    display: flex; flex-direction: column; justify-content: center; align-items: center;
  }
  .ad--square .ad__band { top: 246px; height: 134px; }
  .ad--portrait .ad__band { top: 332px; height: 182px; }

  .ad__headline {
    font-weight: 800;
    line-height: 0.92;
    letter-spacing: -0.5px;
    text-transform: uppercase;
  }
  .ad--square .ad__headline { font-size: 45px; }
  .ad--portrait .ad__headline { font-size: 60px; }

  .ad__message { font-weight: 400; line-height: 1.1; }
  .ad--square .ad__message { font-size: 24px; margin-top: 1px; }
  .ad--portrait .ad__message { font-size: 31px; margin-top: 2px; }

  .ad__footer {
    position: absolute; left: 0; width: 100%; bottom: 0;
    color: var(--brand-blue);
  }
  .ad--square .ad__footer { top: 380px; }
  .ad--portrait .ad__footer { top: 514px; }

  .ad__cta {
    position: absolute; left: 0; width: 100%;
    text-align: center; font-weight: 800; text-transform: uppercase;
  }
  .ad--square .ad__cta { top: 14px; font-size: 18px; }
  .ad--portrait .ad__cta { top: 19px; font-size: 18.5px; }

  .ad__firm {
    position: absolute; display: flex; align-items: center; gap: 8px;
    font-weight: 700; white-space: nowrap;
  }
  .ad__firm-dot {
    width: 12px; height: 12px; border-radius: 50%;
    background: var(--brand-blue); flex: none;
  }
  .ad--square .ad__firm { left: 27px; top: 84px; font-size: 15px; }
  .ad--portrait .ad__firm { left: 43px; top: 97px; font-size: 15px; }

  .ad__contact {
    position: absolute; text-align: right;
  }
  .ad--square .ad__contact { right: 27px; top: 62px; }
  .ad--portrait .ad__contact { right: 43px; top: 72px; }

  .ad__phone { font-weight: 800; line-height: 1; letter-spacing: -0.3px; }
  .ad--square .ad__phone { font-size: 31px; }
  .ad--portrait .ad__phone { font-size: 33px; }

  .ad__web { font-weight: 400; line-height: 1.1; }
  .ad--square .ad__web { font-size: 14px; }
  .ad--portrait .ad__web { font-size: 14.5px; }

  .ad__compliance {
    position: absolute; left: 0; width: 100%;
    text-align: center; color: var(--ink); font-size: 10.5px;
  }
  .ad--square .ad__compliance { top: 125px; }
  .ad--portrait .ad__compliance { top: 146px; }
</style>
</head>
<body>

  <article class="ad ad--square">
    <div class="ad__photo" role="img" aria-label="Portrait photo of the firm's two attorneys in suits against a light grey studio backdrop"></div>
    <section class="ad__band">
      <h1 class="ad__headline">HOA Violating<br>Your Rights?</h1>
      <p class="ad__message">We sue HOAs for Homeowners.</p>
    </section>
    <footer class="ad__footer">
      <p class="ad__cta">Contact us today for a consultation!</p>
      <div class="ad__firm"><span class="ad__firm-dot"></span>Lindqvist Harrow, P.A.</div>
      <div class="ad__contact">
        <p class="ad__phone">1-800-555-0148</p>
        <p class="ad__web">www.covenantshieldcounsel.example</p>
      </div>
      <p class="ad__compliance">Serving Homeowners in Florida with our main office in Miami-Dade.</p>
    </footer>
  </article>

  <article class="ad ad--portrait">
    <div class="ad__photo" role="img" aria-label="Portrait photo of the firm's two attorneys in suits, one with arms crossed, against a light grey studio backdrop"></div>
    <section class="ad__band">
      <h1 class="ad__headline">HOA Violating<br>Your Rights?</h1>
      <p class="ad__message">We sue HOAs for Homeowners.</p>
    </section>
    <footer class="ad__footer">
      <p class="ad__cta">Contact us today for a consultation!</p>
      <div class="ad__firm"><span class="ad__firm-dot"></span>Lindqvist Harrow, P.A.</div>
      <div class="ad__contact">
        <p class="ad__phone">1-800-555-0148</p>
        <p class="ad__web">www.covenantshieldcounsel.example</p>
      </div>
      <p class="ad__compliance">Serving Homeowners in Florida with our main office in Miami-Dade.</p>
    </footer>
  </article>

</body>
</html>
```